Brightpath Property College Needs Banner Designs

I just launched an online real estate school at www.brightpathpropertycollege.com

I am seeking designers to work on 2 banners (listed seperately) as well as a a Facebook design. This listing is for 1 of 2 banners.

First banner I intend to use on different job offering web sites. So "Launch your career into Real Estate" could be the concept. i'm open to 1 sentence pitch's. please look at my website to view graphics and colors.

```html
<!DOCTYPE html>
<html lang="en">
<head>
<meta charset="utf-8">
<title>Brightpath Property College – Launch your career into Real Estate</title>
<link rel="stylesheet" href="https://fonts.googleapis.com/css2?family=Roboto:ital,wght@0,400;0,700;0,900;1,900&display=swap">
<style>
  :root {
    --cream: #fdf6e4;
    --gold-light: #fbe3a6;
    --gold: #f5c651;
    --amber: #eaa624;
    --brown: #3b2a12;
    --ink: #2c2c2c;
    --button-top: #fde27a;
    --button-bottom: #e7a416;
    --button-edge: #b77d0b;
    --photo-sky: #8fb2d6;
    --photo-house: #8a6a52;
    --photo-lawn: #5f7f3a;
    --frame: #c9b99a;
  }
  * { margin: 0; padding: 0; box-sizing: border-box; }
  html, body { width: 1200px; height: 148px; overflow: hidden; background: #ffffff; }

  .banner {
    position: relative;
    width: 1200px;
    height: 148px;
    overflow: hidden;
    font-family: "Roboto", Arial, sans-serif;
    background:
      radial-gradient(ellipse 360px 200px at 760px 160px, rgba(255,255,255,0.55), rgba(255,255,255,0) 70%),
      linear-gradient(90deg, #ffffff 0%, var(--cream) 22%, var(--gold-light) 45%, var(--gold) 62%, var(--amber) 74%, var(--gold-light) 84%, #ffffff 90%, #ffffff 100%);
  }

  .house-photo {
    position: absolute;
    left: 4px;
    top: 4px;
    width: 268px;
    height: 140px;
    border-radius: 12px;
    border: 2px solid var(--frame);
    background: linear-gradient(180deg, var(--photo-sky) 0%, #b7c9dc 30%, var(--photo-house) 48%, #a48669 72%, var(--photo-lawn) 88%, #4d6a2e 100%);
  }

  .headline {
    position: absolute;
    left: 320px;
    top: 22px;
    color: var(--ink);
  }
  .headline__lead {
    display: block;
    font-weight: 400;
    font-size: 28px;
    letter-spacing: 0.5px;
    line-height: 34px;
  }
  .headline__main {
    display: block;
    font-weight: 900;
    font-style: italic;
    font-size: 68px;
    line-height: 72px;
    color: var(--brown);
    letter-spacing: 0.5px;
    margin-left: 2px;
  }

  .cta-button {
    position: absolute;
    left: 755px;
    top: 54px;
    width: 171px;
    height: 45px;
    border-radius: 8px;
    border: 2px solid var(--button-edge);
    background: linear-gradient(180deg, var(--button-top) 0%, var(--gold) 50%, var(--button-bottom) 100%);
    display: flex;
    align-items: center;
    justify-content: center;
    gap: 10px;
    font-weight: 700;
    font-size: 24px;
    color: #1e1e1e;
    text-decoration: none;
    box-shadow: 0 2px 3px rgba(0,0,0,0.3);
  }
  .cta-button svg { width: 14px; height: 16px; }

  .brand {
    position: absolute;
    left: 985px;
    top: 18px;
    width: 200px;
    display: flex;
    flex-direction: column;
    align-items: center;
    gap: 8px;
    text-align: center;
  }
  .brand__dot {
    width: 34px;
    height: 34px;
    border-radius: 50%;
    background: var(--brown);
  }
  .brand__name {
    font-weight: 900;
    font-size: 22px;
    line-height: 24px;
    color: var(--brown);
  }
</style>
</head>
<body>
  <div class="banner">
    <div class="house-photo" role="img" aria-label="Photo of a two-storey family home with a garage and front lawn"></div>

    <h1 class="headline">
      <span class="headline__lead">Launch your career into</span>
      <span class="headline__main">Real Estate</span>
    </h1>

    <a class="cta-button" href="https://www.brightpathpropertycollege.com">
      <svg viewBox="0 0 14 16" aria-hidden="true"><path d="M1 1 L13 8 L1 15 Z" fill="#d92d20"/></svg>
      click here
    </a>

    <div class="brand">
      <span class="brand__dot" aria-hidden="true"></span>
      <span class="brand__name">Brightpath Property College</span>
    </div>
  </div>
</body>
</html>
```